Example of School Sign for Digital Siganage

We sell digital signage software and screens. I have an expo coming up and I want some examples of typical images and messages that a school might use on an outdoor screen for public viewing. The resolution of the screen is quite low at 504 pixels wide by 336 pixels high. This means that we cannot use anything too small or detailed. The images could however be created at 1008 x 672 and that way they will scale down. The images need to be delivered in .psd format with all layers available.

We will call the School Stonemeadow Academy. We want the school name on all the images (slides) and a fictitious logo associated with the name. Examples of the images required would be. . .

1. Congratulations to Lydia Pranter School Dux 2015. (This would have an image of a smiling teenage girl.)

2. Team of the Week. Year 10 Girls under 16 Soccer Team. 5-Wins 0-Losses. (This would have a picture of girls playing soccer.)

3. School Production of Tinsel. August 12th -17th. Get your tickets from the office . (An image of a Tinsel logo)

4. Car Wash at School the Sunday to raise funds for the Year 9 Singapore Trip. (Image of students washing a car)

5. School Holidays Start Friday the 8th of September. School re-opens Monday 25th of September. (An image of a crowd of happy students)

6. Student of the Week. Owen Blakely, Winner of the Frontier Machina Trophy. (image of teenage student with robot)

Hopefully this is clear.

Industry/Entity Type

Digital Signage

Font styles to use
Sans Serif

Requirements
Must have
• School Name and Logo
Should not have
• Any very small fonts or too much fine detail

```html
<!DOCTYPE html>
<html lang="en">
<head>
<meta charset="utf-8">
<title>Student of the Week – Stonemeadow Academy</title>
<link rel="stylesheet" href="https://fonts.googleapis.com/css2?family=Roboto+Condensed:wght@400;700&family=Fredoka:wght@600&display=swap">
<style>
  :root {
    --backdrop: #58585a;
    --sky-deep: #0a86d2;
    --sky-mid: #1ea6e6;
    --sky-light: #56c8f4;
    --headline: #ffffff;
    --subline: #c4e9fb;
    --wave-green: #0f6a4c;
    --paper: #ffffff;
    --sponsor-lilac: #d6a8d8;
    --school-navy: #1d3a78;
    --photo-dark: #4a5358;
    --photo-light: #d9e3ea;
  }
  * { margin: 0; padding: 0; box-sizing: border-box; }
  html, body {
    width: 1200px;
    height: 890px;
    overflow: hidden;
    background: var(--backdrop);
  }
  .sign {
    position: absolute;
    left: 88px;
    top: 109px;
    width: 1011px;
    height: 675px;
    overflow: hidden;
    background: radial-gradient(ellipse at 62% 45%, var(--sky-light) 0%, var(--sky-mid) 40%, var(--sky-deep) 100%);
  }
  .feature-photo {
    position: absolute;
    left: 497px;
    top: 22px;
    width: 514px;
    height: 540px;
    border-radius: 40px 0 0 0;
    background: linear-gradient(100deg, var(--photo-dark) 0%, #6d777c 45%, var(--photo-light) 70%, #8aa0b8 100%);
  }
  .wave {
    position: absolute;
    left: 0;
    top: 0;
    width: 1011px;
    height: 675px;
  }
  .headline {
    position: absolute;
    left: 52px;
    top: 58px;
    font-family: "Roboto Condensed", sans-serif;
    font-weight: 700;
    font-size: 70px;
    line-height: 1;
    color: var(--headline);
    letter-spacing: 0.5px;
  }
  .achievement {
    position: absolute;
    left: 60px;
    top: 148px;
    font-family: "Roboto Condensed", sans-serif;
    font-weight: 400;
    font-size: 48px;
    line-height: 57px;
    color: var(--subline);
  }
  .sponsor {
    position: absolute;
    left: 30px;
    top: 505px;
    width: 320px;
    text-align: center;
    font-family: "Fredoka", sans-serif;
    font-weight: 600;
    font-size: 34px;
    line-height: 49px;
    color: var(--sponsor-lilac);
  }
  .school-name {
    position: absolute;
    right: 32px;
    top: 566px;
    display: flex;
    align-items: center;
    gap: 14px;
    font-family: "Roboto Condensed", sans-serif;
    font-weight: 700;
    color: var(--school-navy);
  }
  .school-name .mark {
    width: 22px;
    height: 22px;
    background: var(--school-navy);
  }
  .school-name .words {
    text-align: right;
    line-height: 1;
  }
  .school-name .line-main { display: block; font-size: 42px; }
  .school-name .line-sub { display: block; font-size: 28px; margin-top: 4px; }
</style>
</head>
<body>
  <main class="sign">
    <div class="feature-photo" role="img" aria-label="Photo of a smiling teenage student giving a thumbs up beside a vintage toy robot"></div>

    <svg class="wave" viewBox="0 0 1011 675" aria-hidden="true">
      <path fill="var(--wave-green)" d="M0 445 C 160 405, 330 425, 500 470 C 640 508, 760 530, 860 500 C 930 478, 980 458, 1011 450 L 1011 675 L 0 675 Z"/>
      <path fill="var(--paper)" d="M0 481 C 170 440, 340 460, 510 505 C 640 540, 770 560, 870 530 C 935 510, 985 490, 1011 482 L 1011 675 L 0 675 Z"/>
    </svg>

    <h1 class="headline">STUDENT OF THE WEEK</h1>
    <p class="achievement">OWEN BLAKELY,<br>WINNER OF<br>THE FRONTIER<br>MACHINA TROPHY.</p>

    <p class="sponsor">HERE IS<br>COMPANY LOGO<br>www.brightpanel.com</p>

    <div class="school-name">
      <span class="mark"></span>
      <span class="words">
        <span class="line-main">Stonemeadow</span>
        <span class="line-sub">Academy</span>
      </span>
    </div>
  </main>
</body>
</html>
```